Dietary supplement products need label designs

We are looking for the design of labels for a 3-in-1 functional dietary supplement product. The purpose of this product is to benefit the pain of the joint, mainly caused by Gout.

They are all natural, plants based, safe and highly effective " one of the kind " product. Product # 1 (in bottle sachet package) is all natural plants based to treat/reduce Gout symptoms; Product #2 (in bottle or sachet package) is all natural enzyme to prevent Gout symptoms; and product #3 (in bottle or sachet) is all natural plants based to maintain the healthy level.

All three products will then be put into one mini-gift box.

The scene is unique, all natural and effective.

Thank you.

Reason: All the current designs are good in their own ways. The one thing that we are still looking for is the combination of natural yet premium products feeling.

```html
<!DOCTYPE html>
<html lang="en">
<head>
<meta charset="utf-8">
<title>Verdell Healthcare – Product 1 Label</title>
<link rel="stylesheet" href="https://fonts.googleapis.com/css2?family=Montserrat:wght@600&family=Questrial&display=swap">
<style>
  :root {
    --backdrop: #b9b9b9;
    --label-light: #2b8f2f;
    --label-mid: #1d6f25;
    --label-dark: #0f4a17;
    --ink-light: #ffffff;
    --grass-light: #8fd84a;
    --grass-dark: #3f9a22;
  }
  html, body {
    margin: 0;
    width: 1200px;
    height: 1200px;
    overflow: hidden;
    background: var(--backdrop);
  }
  .canvas {
    position: relative;
    width: 1200px;
    height: 1200px;
    background: radial-gradient(circle at 50% 45%, #d2d2d2 0%, var(--backdrop) 70%);
  }
  .label {
    position: absolute;
    left: 120px;
    top: 256px;
    width: 960px;
    height: 688px;
    overflow: hidden;
    background: radial-gradient(ellipse at 50% 45%, var(--label-light) 0%, var(--label-mid) 45%, var(--label-dark) 100%);
    color: var(--ink-light);
    text-align: center;
  }
  .brand {
    position: absolute;
    top: 84px;
    left: 0;
    right: 0;
    display: flex;
    justify-content: center;
    align-items: center;
    gap: 14px;
    font-family: "Montserrat", sans-serif;
    font-weight: 600;
    font-size: 34px;
    line-height: 1;
    color: var(--ink-light);
  }
  .brand-mark {
    width: 22px;
    height: 22px;
    background: var(--ink-light);
  }
  .product-title {
    position: absolute;
    top: 236px;
    left: 0;
    right: 0;
    margin: 0;
    font-family: "Montserrat", sans-serif;
    font-weight: 600;
    font-size: 94px;
    line-height: 1;
    letter-spacing: 1px;
  }
  .product-copy {
    position: absolute;
    top: 376px;
    left: 150px;
    right: 150px;
    margin: 0;
    font-family: "Questrial", sans-serif;
    font-size: 17px;
    line-height: 24px;
    text-align: justify;
    text-align-last: center;
  }
  .product-volume {
    position: absolute;
    top: 504px;
    left: 0;
    right: 0;
    margin: 0;
    font-family: "Montserrat", sans-serif;
    font-weight: 600;
    font-size: 40px;
    line-height: 1;
  }
  .grass-band {
    position: absolute;
    left: 0;
    right: 0;
    bottom: 0;
    height: 140px;
    background: linear-gradient(to bottom, rgba(143,216,74,0) 0%, var(--grass-light) 40%, var(--grass-dark) 100%);
  }
</style>
</head>
<body>
  <main class="canvas">
    <section class="label">
      <div class="brand">
        <span class="brand-mark"></span>
        <span class="brand-name">Verdell Healthcare</span>
      </div>
      <h1 class="product-title">PRODUCT 1</h1>
      <p class="product-copy">Lorem ipsum dolor sit amet, consectetur adipisicing elit, sed do eiusmod tempor incididunt ut labore et dolore magna aliqua. Ut enim ad minim veniam, quis nostrud exercitation.</p>
      <p class="product-volume">150CC</p>
      <div class="grass-band" role="img" aria-label="Strip of fresh green grass along the bottom of the label"></div>
    </section>
  </main>
</body>
</html>
```